Fibromyalgia course needing google word doc design for content for course takers

We are in need of a google word doc design for new course for content please see attached logo for colors and look

```html
<!DOCTYPE html>
<html lang="en">
<head>
<meta charset="utf-8">
<title>Steady Days – Course Document Templates</title>
<link href="https://fonts.googleapis.com/css2?family=Montserrat:wght@400;500;600;700&display=swap" rel="stylesheet">
<style>
  :root {
    --backdrop: #dde2e6;
    --paper: #ffffff;
    --navy: #1f1a5c;
    --purple: #7a1fb0;
    --lilac: #bf94da;
    --magenta: #ff2fb4;
    --peach: #ffa574;
    --line-indigo: #3a2bb0;
    --sun: #ffe94a;
  }
  * { box-sizing: border-box; margin: 0; padding: 0; }
  html, body { width: 1200px; height: 978px; overflow: hidden; }
  body {
    position: relative;
    background: var(--backdrop);
    font-family: "Montserrat", Arial, sans-serif;
    color: var(--navy);
  }
  .defs { position: absolute; width: 0; height: 0; }

  .page {
    position: absolute;
    background: var(--paper);
    overflow: hidden;
  }
  .page-art { position: absolute; inset: 0; width: 100%; height: 100%; }

  /* Cover */
  .cover { left: 111px; top: 129px; width: 398px; height: 556px; }
  .cover .brand-name {
    position: absolute; left: 72px; top: 137px; width: 118px;
    font-size: 16.5px; font-weight: 600; color: var(--purple); white-space: nowrap;
  }
  .cover .doc-title {
    position: absolute; left: 74px; top: 201px;
    font-size: 24px; font-weight: 700; letter-spacing: -0.2px; white-space: nowrap;
  }
  .cover .doc-subtitle {
    position: absolute; left: 74px; top: 237px;
    font-size: 12.3px; font-weight: 600;
  }

  /* Inner pages */
  .inner { width: 264px; height: 369px; }
  .page-body-a { left: 581px; top: 129px; }
  .page-closing { left: 863px; top: 129px; width: 260px; height: 363px; }
  .page-columns { left: 581px; top: 539px; }

  .inner .brand-name {
    position: absolute; font-size: 8.3px; font-weight: 600; color: var(--purple); white-space: nowrap;
  }
  .inner .section-heading {
    position: absolute; font-size: 11.6px; font-weight: 600;
  }
  .copy {
    position: absolute; font-size: 3.6px; line-height: 5.85px; font-weight: 500; color: var(--navy);
  }
  .copy p { margin-bottom: 6.5px; }
  .page-number {
    position: absolute; left: 247px; top: 345px; font-size: 7.5px; font-weight: 500;
  }

  .page-body-a .brand-name, .page-columns .brand-name { left: 180px; top: 63px; }
  .page-body-a .section-heading, .page-columns .section-heading { left: 43px; top: 83px; }
  .page-body-a .copy { left: 43px; top: 104px; width: 180px; }

  .page-closing .brand-name { left: 181px; top: 73px; }
  .page-closing .section-heading { left: 40px; top: 111px; }
  .page-closing .copy { left: 40px; top: 131px; width: 180px; }
  .page-closing .copy .recap { margin-bottom: 17px; }
  .page-closing .copy .pillars { margin-bottom: 11px; }

  .signature {
    position: absolute; left: 162px; top: 261px; font-size: 4.4px; line-height: 5.8px;
  }
  .signature .role { color: var(--magenta); }
  .signature .site { color: var(--navy); border-bottom: 0.6px solid var(--purple); padding-bottom: 1px; }

  .contact-row {
    position: absolute; left: 84px; top: 305px; display: flex; gap: 8px;
    font-size: 2.6px; line-height: 3.3px; color: var(--navy);
  }
  .contact-item { display: flex; align-items: flex-start; gap: 1.5px; }
  .contact-item svg { width: 3.4px; height: 3.4px; flex: none; }

  .page-columns .lead { left: 43px; top: 104px; width: 180px; }
  .page-columns .col-left { left: 43px; top: 150px; width: 76px; }
  .page-columns .col-left p { margin-bottom: 10px; }
  .page-columns .col-right { left: 134px; top: 150px; width: 77px; }
  .feature-image {
    position: absolute; left: 134px; top: 248px; width: 97px; height: 81px;
    background: linear-gradient(90deg, var(--sun) 0%, #ff9a8a 45%, var(--magenta) 100%);
  }
</style>
</head>
<body>

<svg class="defs" aria-hidden="true">
  <defs>
    <linearGradient id="ring-sunset" x1="0" y1="0" x2="1" y2="1">
      <stop offset="0" stop-color="#ffa574"/>
      <stop offset="0.55" stop-color="#ff6f9c"/>
      <stop offset="1" stop-color="#ff2fb4"/>
    </linearGradient>
    <linearGradient id="ball-sunset" x1="0" y1="0" x2="1" y2="1">
      <stop offset="0" stop-color="#ffb074"/>
      <stop offset="1" stop-color="#ff4fa8"/>
    </linearGradient>
    <linearGradient id="ring-pink" x1="0" y1="0" x2="0" y2="1">
      <stop offset="0" stop-color="#ff5fc4"/>
      <stop offset="1" stop-color="#ff2fb4"/>
    </linearGradient>
    <path id="arrow-lg" d="M0 -3 L4 0 L0 3 Z" fill="#7a1fb0"/>
    <path id="arrow-sm" d="M0 -2 L2.8 0 L0 2 Z" fill="#7a1fb0"/>
    <circle id="dot-lg" r="2.6" fill="#7a1fb0"/>
    <circle id="dot-sm" r="1.9" fill="#7a1fb0"/>
    <circle id="dot-xs" r="1.2" fill="#7a1fb0"/>
  </defs>
</svg>

<!-- Cover page -->
<section class="page cover">
  <svg class="page-art" viewBox="0 0 398 556" aria-hidden="true">
    <rect x="2" y="81" width="25" height="61" fill="var(--purple)"/>
    <circle cx="349" cy="46" r="39" fill="none" stroke="var(--lilac)" stroke-width="20"/>
    <g>
      <use href="#dot-lg" x="362" y="140"/><use href="#dot-lg" x="374" y="140"/><use href="#dot-lg" x="386" y="140"/><use href="#dot-lg" x="398" y="140"/>
      <use href="#dot-lg" x="362" y="152"/><use href="#dot-lg" x="374" y="152"/><use href="#dot-lg" x="386" y="152"/><use href="#dot-lg" x="398" y="152"/>
      <use href="#dot-lg" x="362" y="164"/><use href="#dot-lg" x="374" y="164"/><use href="#dot-lg" x="386" y="164"/><use href="#dot-lg" x="398" y="164"/>
      <use href="#dot-lg" x="362" y="176"/><use href="#dot-lg" x="374" y="176"/><use href="#dot-lg" x="386" y="176"/><use href="#dot-lg" x="398" y="176"/>
      <use href="#dot-lg" x="362" y="188"/><use href="#dot-lg" x="374" y="188"/><use href="#dot-lg" x="386" y="188"/><use href="#dot-lg" x="398" y="188"/>
    </g>
    <circle cx="131" cy="106" r="18" fill="var(--magenta)"/>
    <g>
      <use href="#arrow-lg" x="75" y="191"/><use href="#arrow-lg" x="90.5" y="191"/><use href="#arrow-lg" x="106" y="191"/>
      <use href="#arrow-lg" x="121.5" y="191"/><use href="#arrow-lg" x="137" y="191"/><use href="#arrow-lg" x="152.5" y="191"/>
      <use href="#arrow-lg" x="168" y="191"/><use href="#arrow-lg" x="183.5" y="191"/><use href="#arrow-lg" x="199" y="191"/>
    </g>
    <circle cx="131" cy="472" r="183" fill="none" stroke="url(#ring-sunset)" stroke-width="19"/>
    <circle cx="102" cy="340" r="11" fill="none" stroke="url(#ring-pink)" stroke-width="9"/>
    <g>
      <use href="#dot-sm" x="148" y="329"/><use href="#dot-sm" x="157.7" y="329"/><use href="#dot-sm" x="167.4" y="329"/><use href="#dot-sm" x="177.1" y="329"/><use href="#dot-sm" x="186.8" y="329"/>
      <use href="#dot-sm" x="148" y="338.5"/><use href="#dot-sm" x="157.7" y="338.5"/><use href="#dot-sm" x="167.4" y="338.5"/><use href="#dot-sm" x="177.1" y="338.5"/>
      <use href="#dot-sm" x="148" y="348"/><use href="#dot-sm" x="157.7" y="348"/><use href="#dot-sm" x="167.4" y="348"/>
      <use href="#dot-sm" x="148" y="357.5"/><use href="#dot-sm" x="157.7" y="357.5"/>
      <use href="#dot-sm" x="148" y="367"/>
    </g>
    <circle cx="96" cy="558" r="154" fill="none" stroke="var(--line-indigo)" stroke-width="0.9"/>
    <circle cx="83" cy="405" r="14" fill="url(#ball-sunset)"/>
    <circle cx="188" cy="428" r="6.5" fill="url(#ball-sunset)"/>
    <rect x="374" y="434" width="24" height="61" fill="var(--purple)"/>
  </svg>
  <div class="brand-name">Steady Days</div>
  <h1 class="doc-title">type document here</h1>
  <p class="doc-subtitle">subtitle here</p>
</section>

<!-- Inner page: full-width body copy -->
<section class="page inner page-body-a">
  <svg class="page-art" viewBox="0 0 264 369" aria-hidden="true">
    <circle cx="78" cy="7" r="40" fill="none" stroke="url(#ring-pink)" stroke-width="4"/>
    <circle cx="254" cy="10" r="13.5" fill="none" stroke="var(--lilac)" stroke-width="9"/>
    <rect x="1" y="54" width="16" height="40" fill="var(--purple)"/>
    <circle cx="208" cy="50" r="9" fill="var(--magenta)"/>
    <g>
      <use href="#arrow-sm" x="75" y="69"/><use href="#arrow-sm" x="85" y="69"/><use href="#arrow-sm" x="95" y="69"/>
      <use href="#arrow-sm" x="105" y="69"/><use href="#arrow-sm" x="115" y="69"/><use href="#arrow-sm" x="125" y="69"/>
      <use href="#arrow-sm" x="135" y="69"/><use href="#arrow-sm" x="145" y="69"/><use href="#arrow-sm" x="155" y="69"/>
    </g>
    <g>
      <use href="#dot-sm" x="241" y="94"/><use href="#dot-sm" x="251" y="94"/><use href="#dot-sm" x="261" y="94"/>
      <use href="#dot-sm" x="241" y="104"/><use href="#dot-sm" x="251" y="104"/><use href="#dot-sm" x="261" y="104"/>
      <use href="#dot-sm" x="241" y="114"/><use href="#dot-sm" x="251" y="114"/><use href="#dot-sm" x="261" y="114"/>
      <use href="#dot-sm" x="241" y="124"/><use href="#dot-sm" x="251" y="124"/><use href="#dot-sm" x="261" y="124"/>
    </g>
    <rect x="248" y="289" width="16" height="40" fill="var(--purple)"/>
    <circle cx="34" cy="454" r="115" fill="none" stroke="var(--line-indigo)" stroke-width="0.7"/>
    <circle cx="32" cy="340" r="8" fill="url(#ball-sunset)"/>
    <circle cx="96" cy="354" r="4" fill="url(#ball-sunset)"/>
  </svg>
  <div class="brand-name">Steady Days</div>
  <h2 class="section-heading">heading</h2>
  <div class="copy">
    <p>Welcome to the course. Each module explains one part of living with fibromyalgia in clear, simple steps. You will learn how pain signals work, why sleep and stress matter, and which small daily habits can ease flare days. Read at your own pace, take notes in the margins, and return to any lesson whenever you need a reminder. Short exercises close every section so you can practise what you read.</p>
    <p>Pacing is the first skill we cover. Many people push hard on good days and then lose the next three days to pain and fatigue. Pacing means planning activity in smaller blocks with rest built in before you feel drained. Start by tracking your energy for one week, noting tasks, rest breaks and symptom levels. Patterns soon appear, and they show where your limits sit today. From there you can raise activity slowly, about ten percent at a time, so your body adapts without a crash. Keep the log simple so it stays useful over time.</p>
    <p>Sleep is the second focus. Poor sleep and pain feed each other, so improving one often helps the other. Aim for a steady bedtime and wake time, even on weekends. Keep the bedroom cool, dark and quiet, and leave screens outside for the last hour of the evening. A warm shower, light stretching or slow breathing can signal to the body that rest is near. If you wake in the night, get up after twenty minutes, sit somewhere calm and return when drowsy. Caffeine after lunch, heavy meals late at night and long daytime naps can all make sleep lighter. Try one change at a time and note how you feel after each week. Small shifts add up, and many course members report clearer mornings within a month. If sleep stays broken despite these steps, talk with your doctor, since other conditions such as sleep apnoea or restless legs can overlap with fibromyalgia and may need their own care plan. Your notes from this module will help that conversation.</p>
    <p>Gentle movement is the third pillar. Exercise may seem like the last thing you want during a flare, yet regular low impact activity can lower pain over time. Walking, water exercise, tai chi and easy cycling are good places to begin. Start with five minutes and add a minute or two each week. Warm up slowly, stay below the point where pain sharply rises, and cool down with light stretches. Expect some soreness at first; it should fade within a day. If it lasts longer, scale back and build again more slowly. Pair movement with pacing and sleep habits from earlier modules, and keep recording results in your log. Over weeks you will see which types of movement suit your body best, and which times of day feel easiest for you.</p>
  </div>
  <div class="page-number">1.</div>
</section>

<!-- Inner page: closing summary with contact row -->
<section class="page inner page-closing">
  <svg class="page-art" viewBox="0 0 260 363" aria-hidden="true">
    <circle cx="76" cy="7" r="40" fill="none" stroke="url(#ring-pink)" stroke-width="4"/>
    <circle cx="249" cy="10" r="13.5" fill="none" stroke="var(--lilac)" stroke-width="9"/>
    <rect x="1" y="53" width="16" height="40" fill="var(--purple)"/>
    <circle cx="209" cy="60" r="9" fill="var(--magenta)"/>
    <g>
      <use href="#arrow-sm" x="78" y="80"/><use href="#arrow-sm" x="88" y="80"/><use href="#arrow-sm" x="98" y="80"/>
      <use href="#arrow-sm" x="108" y="80"/><use href="#arrow-sm" x="118" y="80"/><use href="#arrow-sm" x="128" y="80"/>
      <use href="#arrow-sm" x="138" y="80"/><use href="#arrow-sm" x="148" y="80"/><use href="#arrow-sm" x="158" y="80"/>
    </g>
    <g>
      <use href="#dot-sm" x="236" y="91"/><use href="#dot-sm" x="246" y="91"/><use href="#dot-sm" x="256" y="91"/>
      <use href="#dot-sm" x="236" y="101"/><use href="#dot-sm" x="246" y="101"/><use href="#dot-sm" x="256" y="101"/>
      <use href="#dot-sm" x="236" y="111"/><use href="#dot-sm" x="246" y="111"/><use href="#dot-sm" x="256" y="111"/>
      <use href="#dot-sm" x="236" y="121"/><use href="#dot-sm" x="246" y="121"/><use href="#dot-sm" x="256" y="121"/>
    </g>
    <circle cx="47" cy="264" r="6.5" fill="none" stroke="url(#ring-pink)" stroke-width="5"/>
    <g>
      <use href="#dot-xs" x="78" y="257"/><use href="#dot-xs" x="84" y="257"/><use href="#dot-xs" x="90" y="257"/><use href="#dot-xs" x="96" y="257"/><use href="#dot-xs" x="102" y="257"/>
      <use href="#dot-xs" x="78" y="263"/><use href="#dot-xs" x="84" y="263"/><use href="#dot-xs" x="90" y="263"/><use href="#dot-xs" x="96" y="263"/>
      <use href="#dot-xs" x="78" y="269"/><use href="#dot-xs" x="84" y="269"/><use href="#dot-xs" x="90" y="269"/>
      <use href="#dot-xs" x="78" y="275"/><use href="#dot-xs" x="84" y="275"/>
      <use href="#dot-xs" x="78" y="281"/>
    </g>
    <rect x="244" y="284" width="16" height="40" fill="var(--purple)"/>
    <circle cx="30" cy="435" r="115" fill="none" stroke="var(--line-indigo)" stroke-width="0.7"/>
    <circle cx="28" cy="320" r="8.5" fill="url(#ball-sunset)"/>
    <circle cx="97" cy="336" r="4" fill="url(#ball-sunset)"/>
  </svg>
  <div class="brand-name">Steady Days</div>
  <h2 class="section-heading">heading</h2>
  <div class="copy">
    <p class="recap">Thank you for joining the course. This page gathers the key points from the module so you can review them quickly. Keep it near your planner or print it for the fridge door. Each point links back to a full lesson if you want more detail, worked examples and practice sheets. Share it with family so they understand your plan.</p>
    <p class="pillars">Remember the three pillars: pacing, sleep and gentle movement. None of them works alone, and progress is rarely a straight line. Expect good weeks and hard weeks, and treat setbacks as information rather than failure. Check in with your log every Sunday, choose one goal for the week ahead and keep it small enough to reach even on a tired day.</p>
    <p>Questions about the material can be sent to the course team at any time. We read every message and reply within two working days.</p>
  </div>
  <div class="signature">
    <div class="role">Creative Art Director</div>
    <div class="site">www.steadydays.example</div>
  </div>
  <div class="contact-row">
    <div class="contact-item">
      <svg viewBox="0 0 10 10" aria-hidden="true"><path d="M5 0.5a3.3 3.3 0 0 0-3.3 3.3C1.7 6.3 5 9.5 5 9.5s3.3-3.2 3.3-5.7A3.3 3.3 0 0 0 5 0.5zm0 4.6a1.3 1.3 0 1 1 0-2.6 1.3 1.3 0 0 1 0 2.6z" fill="var(--navy)"/></svg>
      <span>12 Sample Road<br>Riverton, Canada</span>
    </div>
    <div class="contact-item">
      <svg viewBox="0 0 10 10" aria-hidden="true"><path d="M2.2 0.8l1.6 1.9-0.9 1.3c0.6 1.3 1.6 2.3 2.9 2.9l1.3-0.9 1.9 1.6-0.9 1.6C4.6 9.2 0.8 5.4 0.6 1.7z" fill="var(--navy)"/></svg>
      <span>+1 555 010 2000<br>+1 555 010 3000</span>
    </div>
    <div class="contact-item">
      <svg viewBox="0 0 10 10" aria-hidden="true"><rect x="0.5" y="2" width="9" height="6" fill="var(--navy)"/><path d="M0.8 2.3L5 5.5l4.2-3.2" fill="none" stroke="#fff" stroke-width="0.8"/></svg>
      <span>hello@steadydays.example</span>
    </div>
  </div>
</section>

<!-- Inner page: two-column layout with image area -->
<section class="page inner page-columns">
  <svg class="page-art" viewBox="0 0 264 369" aria-hidden="true">
    <circle cx="78" cy="7" r="40" fill="none" stroke="url(#ring-pink)" stroke-width="4"/>
    <circle cx="254" cy="10" r="13.5" fill="none" stroke="var(--lilac)" stroke-width="9"/>
    <rect x="1" y="54" width="16" height="40" fill="var(--purple)"/>
    <circle cx="208" cy="50" r="9" fill="var(--magenta)"/>
    <g>
      <use href="#arrow-sm" x="75" y="69"/><use href="#arrow-sm" x="85" y="69"/><use href="#arrow-sm" x="95" y="69"/>
      <use href="#arrow-sm" x="105" y="69"/><use href="#arrow-sm" x="115" y="69"/><use href="#arrow-sm" x="125" y="69"/>
      <use href="#arrow-sm" x="135" y="69"/><use href="#arrow-sm" x="145" y="69"/><use href="#arrow-sm" x="155" y="69"/>
    </g>
    <g>
      <use href="#dot-sm" x="241" y="94"/><use href="#dot-sm" x="251" y="94"/><use href="#dot-sm" x="261" y="94"/>
      <use href="#dot-sm" x="241" y="104"/><use href="#dot-sm" x="251" y="104"/><use href="#dot-sm" x="261" y="104"/>
      <use href="#dot-sm" x="241" y="114"/><use href="#dot-sm" x="251" y="114"/><use href="#dot-sm" x="261" y="114"/>
      <use href="#dot-sm" x="241" y="124"/><use href="#dot-sm" x="251" y="124"/><use href="#dot-sm" x="261" y="124"/>
    </g>
    <rect x="248" y="288" width="16" height="40" fill="var(--purple)"/>
    <circle cx="34" cy="454" r="115" fill="none" stroke="var(--line-indigo)" stroke-width="0.7"/>
    <circle cx="32" cy="340" r="8" fill="url(#ball-sunset)"/>
    <circle cx="96" cy="354" r="4" fill="url(#ball-sunset)"/>
  </svg>
  <div class="brand-name">Steady Days</div>
  <h2 class="section-heading">heading</h2>
  <div class="copy lead">
    <p>This module looks at stress and the nervous system. Stress does not cause fibromyalgia, but it can turn up the volume on pain. Learning to calm the body on purpose gives you a tool you can use anywhere, at home, at work or in a waiting room. The two columns below set out the basics and a short daily routine.</p>
  </div>
  <div class="copy col-left">
    <p>When the body senses threat it tightens muscles, speeds the heart and sharpens attention. Useful in short bursts, this state drains energy when it lasts all day. Many people with fibromyalgia live close to that edge. Slow breathing, muscle release and guided rest send a safety signal instead, helping muscles soften and easing the load on tired joints.</p>
    <p>Other calming tools include journaling, time in nature, music and gentle company. Choose the ones that fit your life and practise them when you feel well, so they are ready when you need them. Skills grow stronger with repetition, much like muscles. Some people find short audio guides helpful at first; the course library holds several you can try. Most members notice a calmer baseline and easier sleep.</p>
  </div>
  <div class="copy col-right">
    <p>Try this each morning and evening. Sit or lie comfortably and breathe in through the nose for four counts, then out for six. Repeat ten times. Next, tense each muscle group for five seconds and release, moving from feet to shoulders. Finish with two minutes of quiet attention on something pleasant. Record how you feel before and after in your log.</p>
  </div>
  <div class="feature-image" role="img" aria-label="Image area for a calming course photo"></div>
  <div class="page-number">1.</div>
</section>

</body>
</html>
```